Firm of surveyors needs a professional yet friendly looking flyer

Our company offers help to landlords who have a phone mast on their property. We help them to negotiate the best rent and lease terms. There are so many landlords who don't seek professional advice because they don't know it's available. We want to send them a flyer which is informative, looks professional but also friendly so it prompts them to call us. I have attached the wording and some pictures but have more I can send but they were too large to attach.

Target Market(s)

Ranges from farmers to large corporations and land owners

Industry/Entity Type

Surveyor

Font styles to use
Sans Serif

Colors
acd136
9bcb3c
000000
ffffff
606060
848484

Requirements
Must have
• Must be clear, must give a professional look, must include pictures, must include our logo, must use our colour scheme (or variations of it). Ideally, I would like a try-fold design if possible.
Nice to have
• I would like there to be stand out lines to catch the readers eye (I have included some on the wording document). I would like a clean and modern design
Should not have
• Should not be too fussy

```html
<!DOCTYPE html>
<html lang="en">
<head>
<meta charset="utf-8">
<title>Skyline Mast Advisers – Tri-fold Flyer</title>
<link href="https://fonts.googleapis.com/css2?family=PT+Sans:wght@400;700&family=Open+Sans:wght@300;400;600&display=swap" rel="stylesheet">
<style>
:root{
  --green:#4a7232;
  --lime:#9bcb3c;
  --lime-bright:#acd136;
  --black:#000000;
  --white:#ffffff;
  --grey:#606060;
  --grey-light:#848484;
  --backdrop:#a97b4f;
  --heading:"PT Sans",Arial,sans-serif;
  --body:"Open Sans",Arial,sans-serif;
}
*{margin:0;padding:0;box-sizing:border-box}
html,body{width:797px;height:1200px;overflow:hidden}
body{background:var(--backdrop);position:relative;font-family:var(--body);color:var(--black)}
.sheet{position:absolute;left:56px;width:678px;height:528px;display:flex;box-shadow:2px 3px 6px rgba(0,0,0,.35);overflow:hidden}
.sheet--outer{top:58px}
.sheet--inner{top:606px}
.panel{position:relative;height:100%;overflow:hidden}
.panel--wide{width:228px}
.panel--narrow{width:222px}
.panel svg.shape{position:absolute;left:0;top:0}

/* outer: services */
.services{background:var(--green)}
.photo-mast-roof{position:absolute;left:0;top:220px;width:228px;height:308px;background:linear-gradient(180deg,#3e6fc0 0%,#6f9ad8 60%,#b9c9d9 100%)}
.services__title{position:absolute;left:22px;top:22px;font-family:var(--heading);font-weight:700;font-size:20px;color:var(--white)}
.services__list{position:absolute;left:22px;top:52px;list-style:none}
.services__list li{font-size:11px;font-weight:300;color:var(--white);line-height:17.3px;padding-left:13px;position:relative}
.services__list li::before{content:"";position:absolute;left:0;top:5px;width:7px;height:7px;border-radius:50%;background:var(--lime-bright)}

/* outer: contact */
.contact{background:var(--white)}
.contact__lead{position:absolute;left:15px;top:19px;font-family:var(--heading);font-size:16px;line-height:18.5px;color:var(--green)}
.contact__offer{position:absolute;left:15px;top:58px;font-size:13.6px;font-weight:300;line-height:18px;color:var(--green)}
.contact__company{position:absolute;left:15px;top:114px;font-family:var(--heading);font-weight:700;font-size:13px;color:var(--green)}
.contact__address{position:absolute;left:15px;top:137px;font-size:9.4px;line-height:14px;color:#222}
.contact__lines{position:absolute;left:15px;top:172px;list-style:none;font-size:9.4px;line-height:16.4px;color:#222}
.contact__lines span{color:var(--green);display:inline-block;width:13px}
.photo-mast-small{position:absolute;left:8px;top:258px;width:76px;height:96px;background:linear-gradient(180deg,#f4f4f4,#d3d6d9)}
.contact__note{position:absolute;right:18px;top:281px;text-align:right;font-size:13.4px;font-weight:300;line-height:17.6px;color:var(--white);white-space:nowrap}
.contact__call{position:absolute;left:28px;top:462px;font-size:17px;color:var(--white)}
.contact__number{position:absolute;left:27px;top:484px;font-family:var(--heading);font-weight:700;font-size:28px;color:var(--white)}

/* outer: cover */
.cover{background:var(--white)}
.photo-mast-hill{position:absolute;left:0;top:180px;width:228px;height:348px;background:linear-gradient(180deg,#4d86d4 0%,#a9c9ea 55%,#6d9250 75%,#4d6f33 100%)}
.brand{position:absolute;left:0;width:228px;top:46px;display:flex;align-items:center;justify-content:center;gap:6px}
.brand__dot{width:11px;height:11px;border-radius:50%;background:var(--green)}
.brand__name{font-family:var(--heading);font-weight:700;font-size:22px;color:var(--green);letter-spacing:.5px}
.cover__claim{position:absolute;left:0;width:228px;top:121px;text-align:center;font-size:14px;font-weight:300;line-height:18.5px;color:var(--grey)}
.cover__advice{position:absolute;right:20px;top:249px;text-align:right;font-size:13.8px;font-weight:300;line-height:17.6px;color:var(--black);white-space:nowrap}

/* inner */
.copy{background:var(--white);padding:22px 16px 0 17px}
.copy--shaded{background:linear-gradient(90deg,#f7f7f7,#ececec);padding:22px 14px 0 12px}
.copy p{font-size:6.7px;line-height:10.1px;color:#333;text-align:justify;margin-bottom:10px}
.copy--shaded p{color:#555}
.copy h2{font-family:var(--heading);font-weight:400;font-size:17px;line-height:18px;color:var(--green);margin:6px 0 9px}
.offer{background:#2f63b8}
.photo-mast-sky{position:absolute;inset:0;background:linear-gradient(180deg,#1f55b0 0%,#3f78c8 45%,#7fa9dc 100%)}
.offer__head{position:absolute;left:19px;top:17px;font-family:var(--heading);font-weight:700;font-size:25px;line-height:30px;color:var(--white)}
.offer__sub{position:absolute;left:19px;top:82px;font-size:16.5px;color:var(--white)}
.offer__help{position:absolute;left:19px;top:120px;font-size:14.5px;line-height:18px;color:var(--white)}
.offer__help b{font-family:var(--heading);font-size:19.5px}
.offer__help .big{font-size:22px;display:block;margin-top:4px}
.footer{position:absolute;left:0;bottom:0;width:678px;height:80px}
.footer__email{position:absolute;left:106px;bottom:20px;font-size:7.5px;color:var(--white)}
.footer__web{position:absolute;left:240px;bottom:17px;font-family:var(--heading);font-weight:700;font-size:13px;color:var(--white)}
.footer__phone{position:absolute;left:462px;bottom:14px;font-family:var(--heading);font-weight:700;font-size:18px;color:var(--white)}
</style>
</head>
<body>

<section class="sheet sheet--outer">
  <div class="panel panel--wide services">
    <div class="photo-mast-roof" role="img" aria-label="Photo of a rooftop telecom mast against a blue sky"></div>
    <svg class="shape" width="228" height="528" aria-hidden="true">
      <path d="M0 0H228V200Q120 252 0 268Z" fill="#4a7232"/>
      <path d="M0 268Q120 252 228 200V214Q120 264 0 280Z" fill="#000"/>
    </svg>
    <h1 class="services__title">OUR SERVICES</h1>
    <ul class="services__list">
      <li>Rent Reviews</li><li>Lease Renewals</li><li>Network Consolidation Issues</li><li>Site Shares</li><li>Rent Protection</li><li>Equipment Upgrades</li><li>Mast Removals / Decommissioning</li><li>Mast Sales and Marketing</li><li>Land Marketing for Masts</li><li>Mast Management and Portfolios</li><li>Safety Testing</li>
    </ul>
  </div>

  <div class="panel panel--narrow contact">
    <div class="photo-mast-small" role="img" aria-label="Photo of a lattice telecom mast with antennas"></div>
    <svg class="shape" width="222" height="528" aria-hidden="true">
      <path d="M0 460C20 420 120 330 222 236V528H0Z" fill="#4a7232"/>
    </svg>
    <p class="contact__lead">Unsure whether you are<br>getting the best rent?</p>
    <p class="contact__offer">CALL US NOW FOR A FREE,<br>NO OBLIGATION CHAT</p>
    <p class="contact__company">Skyline Mast Advisers Ltd</p>
    <p class="contact__address">Unit 4, Orchard Court, Hillview Business Park,<br>Wenbury, WB7 2QT.</p>
    <ul class="contact__lines">
      <li><span>t :</span> 01632 960418</li>
      <li><span>f :</span> 01632 960419</li>
      <li><span>e :</span> hello@skylinemastadvisers.co.uk</li>
      <li><span>w:</span> www.skylinemastadvisers.co.uk</li>
    </ul>
    <p class="contact__note">Our<br>expert<br>surveyors<br>will be happy<br>to help you<br>understand<br>proposed changes<br>and what they could<br>mean for you</p>
    <p class="contact__call">Call Us</p>
    <p class="contact__number">01632 960418</p>
  </div>

  <div class="panel panel--wide cover">
    <div class="photo-mast-hill" role="img" aria-label="Photo of a tall lattice mast on a grassy hillside under a blue sky"></div>
    <svg class="shape" width="228" height="528" aria-hidden="true">
      <path d="M0 0H228V190Q80 180 0 248Z" fill="#ffffff"/>
      <path d="M0 248Q80 180 228 190V206Q80 196 0 264Z" fill="#9bcb3c"/>
    </svg>
    <div class="brand"><span class="brand__dot"></span><span class="brand__name">SKYLINE MAST</span></div>
    <p class="cover__claim">We act EXCLUSIVELY for<br>landlords on ALL phone<br>mast matters</p>
    <p class="cover__advice">Landlords<br>should not<br>sign<br>anything<br>until they<br>have<br>sought<br>professional<br>advice</p>
  </div>
</section>

<section class="sheet sheet--inner">
  <div class="panel panel--wide copy">
    <p>Skyline Mast Advisers is a firm of telecoms surveyors with over 15 years experience of dealing with mobile phone mast operators. We have built up a massive database of thousands of comparable mobile phone mast deals to aid us in our telecoms negotiations. All our surveyors have spent time working for phone mast operators and know the industry inside out. We now work exclusively for landlords, fighting your corner, ensuring our landlords get the highest rents and best lease terms available in the market place.</p>
    <p>Many of the original mobile phone mast leases / agreements are now coming up for renewal. This is an ideal opportunity for landlords to achieve the best deal. We are currently offering to review telecoms leases for free and provide landlords with our recommendations. If you would like to take us up on this free no obligation offer, send a copy of your agreement and any recent correspondence to us, either via post or email using the details on this flyer. Please also provide us with your name, contact number and let us know the current rent you are achieving so we can see if there is room for improvement. Once we have received this, one of our surveyors will give you a call when convenient to talk through your lease with you, highlighting anything we feel needs addressing, any opportunity to increase the rent, or to discuss a specific issue you are having with your mast (i.e. an upgrade request).</p>
    <p>Recently, operators have been attempting to cut costs by reducing rents. They are joining forces in an effort to drive rents down. Many landlords are contacting us after receiving a letter from the operators / operators agent, telling them they must accept a rent reduction or risk losing their site. In the majority of cases, Skyline Mast Advisers can prevent this from occurring and protect the landlords rental income.</p>
    <h2>Sell your phone mast</h2>
    <p>We can also assist landlords in selling their phone mast. We have strong links with many large investors who regularly purchase the freehold or leasehold interest of masts and will pay a cash lump sum often, even hundreds</p>
  </div>

  <div class="panel panel--narrow copy copy--shaded">
    <p>of thousands of pounds. This can be done in a matter of weeks and the cash is yours to spend however you like, regardless of whether the mast stays for the duration of the investors leasehold or not. We can negotiate flexible terms, such as a buyback option so please call us today to discuss.</p>
    <h2>Getting A Phone Mast</h2>
    <p>If you don't currently have a mast located on your land but are interested in receiving thousands of pounds a year in rental income or you have a redundant mast you would like to market, we offer a free advertising service on our website. We will market your land to phone mast operators with a view to having a mast located there. Please visit the 'Advertise My Site' link on our website to take advantage of this service.</p>
    <h2>The current telecoms<br>climate</h2>
    <p>The telecoms market in relation to mobile phone masts is going through some huge changes. Operators are combining to cut costs. We have already seen Northlink join forces with Tellacom and Vireo form a jointly owned company with Castwave called JTIL. More recently Tellacom and Amberline have merged to form Allways Connect Ltd to become the new network leader. What this can mean for the landlord is changes to their site and potentially the loss of income. It can all be very confusing but don't worry, this is where we can help. We know the telecoms industry and understand how a new situation may affect a landlord, therefore allowing us to provide the best advice on protecting your asset.</p>
    <p>In April 2017 the Government introduced the Digital Economy Act. This sets out significant changes for landlords including the way rents are calculated. We have already seen operators contact landlords trying to reduce their rent in light of this new law. We are working alongside specialist telecoms solicitors to try to reduce the potential negative impact on landlords.</p>
  </div>

  <div class="panel panel--wide offer">
    <div class="photo-mast-sky" role="img" aria-label="Photo of a white monopole mast with panel antennas and dishes against a blue sky"></div>
    <h2 class="offer__head">Interested in<br>selling your site?</h2>
    <p class="offer__sub">Or already have an offer?</p>
    <p class="offer__help"><b>We can help you</b> to<br>achieve the best sale price,<span class="big">quickly</span></p>
  </div>

  <div class="footer">
    <svg width="678" height="80" aria-hidden="true">
      <path d="M0 80V48Q300 -10 678 14V80Z" fill="#9bcb3c"/>
      <path d="M0 80V52Q300 8 678 30V80Z" fill="#000"/>
      <path d="M0 80V58Q300 22 678 40V80Z" fill="#4a7232"/>
    </svg>
    <span class="footer__email">hello@skylinemastadvisers.co.uk</span>
    <span class="footer__web">www.skylinemastadvisers.co.uk</span>
    <span class="footer__phone">01632 960418</span>
  </div>
</section>

</body>
</html>
```